Vorla Advise Business Cards

We need a business card design for Vorla Advise (Logo Attached), a management consultancy specialized in brand & business building.

Design should be clean, smart and a touch of innnovation without being gimmicky.

The details on the card should be:
Name: Tomas Vellaquin
Title: Managing Director
Address: 42 Marden Wharf, Kestrel Tower Building, Singapore 073296
Tel: +6284729156048
email: tv@vorlaadvise.example
website: vorlaadvise.example

For further background on corporate identity, please check www.vorlaadvise.example
Updates

Dear all,

Many thanks for the submissions so far! I gave feedback to those designs that I prefer at this stage.

Overall I see that my preference goes into the direction that 'less is more' and 'simple is beautiful'

Please create uniqueness and standout by the simplicity and attraction of the overall concept and design.

Many thanks and please shout incase of questions!

Tomas

Industry/Entity Type

Business

```html
<!DOCTYPE html>
<html lang="en">
<head>
<meta charset="utf-8">
<title>Vorla Advise Business Cards</title>
<link rel="stylesheet" href="https://fonts.googleapis.com/css2?family=Source+Sans+3:wght@400;600;700&display=swap">
<style>
  :root {
    --orange: #f36c12;
    --orange-deep: #ff6a00;
    --ink: #333333;
    --white: #ffffff;
    --backdrop: #ecebe8;
    --rule: #9a9a9a;
  }
  * { box-sizing: border-box; margin: 0; padding: 0; }
  html, body {
    width: 1174px;
    height: 1200px;
    overflow: hidden;
    background: var(--backdrop);
    font-family: "Source Sans 3", "Myriad Pro", Arial, sans-serif;
  }
  .canvas { position: relative; width: 1174px; height: 1200px; }

  .card {
    position: absolute;
    overflow: hidden;
    box-shadow: 0 4px 14px rgba(0,0,0,0.18);
  }

  /* Front card */
  .card--front {
    left: 202px; top: 39px;
    width: 942px; height: 540px;
    background: var(--white);
  }
  .company-name {
    position: absolute;
    left: 0; right: 0;
    text-align: center;
    font-weight: 600;
    line-height: 1;
  }
  .card--front .company-name {
    top: 104px;
    font-size: 74px;
    color: var(--orange);
  }
  .address {
    position: absolute;
    right: 507px; top: 256px;
    text-align: right;
    font-style: normal;
    font-size: 24px;
    line-height: 42px;
    color: var(--ink);
  }
  .divider {
    position: absolute;
    left: 456px; top: 250px;
    width: 1px; height: 140px;
    background: var(--rule);
  }
  .contacts {
    position: absolute;
    left: 484px; top: 256px;
    list-style: none;
    font-size: 24px;
    line-height: 42px;
    color: var(--ink);
  }
  .contacts li { display: flex; align-items: center; gap: 10px; }
  .contacts svg { width: 18px; height: 18px; flex: none; }
  .base-band { position: absolute; left: 0; top: 0; width: 942px; height: 540px; }
  .holder {
    position: absolute;
    left: 158px; top: 466px;
    color: var(--white);
  }
  .holder__name { font-size: 29px; font-weight: 700; line-height: 34px; }
  .holder__title { font-size: 23px; font-weight: 400; line-height: 30px; }

  /* Back card */
  .card--back {
    left: 26px; top: 623px;
    width: 944px; height: 539px;
    background: var(--orange-deep);
  }
  .card--back .company-name {
    top: 190px;
    font-size: 84px;
    color: var(--white);
  }
  .site {
    position: absolute;
    left: 0; right: 0; top: 376px;
    text-align: center;
    font-size: 25px;
    letter-spacing: 4px;
    color: var(--white);
  }
</style>
</head>
<body>
<main class="canvas">

  <section class="card card--front" aria-label="Business card front">
    <div class="company-name">Vorla Advise</div>

    <address class="address">
      42 Marden Wharf, Kestrel<br>
      Tower Building<br>
      Singapore 073296
    </address>

    <div class="divider"></div>

    <ul class="contacts">
      <li>
        <svg viewBox="0 0 18 18" aria-hidden="true"><circle cx="9" cy="9" r="8" fill="none" stroke="var(--orange)" stroke-width="1.6"/><path d="M6 5 l2 0 l1 2.5 l-1.2 1 a5 5 0 0 0 2.2 2.2 l1 -1.2 l2.5 1 l0 2 a1 1 0 0 1 -1 1 a8 8 0 0 1 -7.5 -7.5 a1 1 0 0 1 1 -1z" fill="var(--orange)"/></svg>
        +6284729156048
      </li>
      <li>
        <svg viewBox="0 0 18 18" aria-hidden="true"><rect x="1" y="4" width="16" height="11" rx="1.5" fill="var(--orange)"/><path d="M2 5 L9 10.5 L16 5" fill="none" stroke="var(--white)" stroke-width="1.5"/></svg>
        tv@vorlaadvise.example
      </li>
      <li>
        <svg viewBox="0 0 18 18" aria-hidden="true"><circle cx="9" cy="9" r="8" fill="var(--orange)"/><path d="M1 9 H17 M9 1 C5 5 5 13 9 17 M9 1 C13 5 13 13 9 17" fill="none" stroke="var(--white)" stroke-width="1.1"/></svg>
        www.vorlaadvise.example
      </li>
    </ul>

    <svg class="base-band" viewBox="0 0 942 540" aria-hidden="true">
      <path d="M0 455 Q 471 405 942 455 L942 540 L0 540 Z" fill="var(--orange)"/>
    </svg>

    <div class="holder">
      <div class="holder__name">Tomas Vellaquin</div>
      <div class="holder__title">Managing Director</div>
    </div>
  </section>

  <section class="card card--back" aria-label="Business card back">
    <div class="company-name">Vorla Advise</div>
    <div class="site">www.vorlaadvise.example</div>
  </section>

</main>
</body>
</html>
```